Digital Billboard Design: Winter Sales Event

I own a boutique furniture store in Calgary, AB (maplewoven.ca) and I am looking to advertise our winter sale event on a new curved digital billboard (specs attached including required file type).

I have this billboard rented for 52-weeks so I will be looking to change the design every 4-weeks (i.e. this is intended to be an ongoing project).

The objective of this first billboard is to raise awareness around our annual winter sales event. The store itself is only a few blocks from the billboard so those commuting into downtown are just a short drive from the store.

I am looking for a fresh, clean, contemporary look that will grab your attention as you drive into downtown Calgary without presenting to much info so as to be distracting (and overwhelming -- the billboard does not need to contain all info on my current marketing material). I should also note that the store caters to a higher-end, more sophisticated clientele so the graphics need to reflect the brand (i.e. we are not Brenton Furniture or Couch Depot!).

I have attached three files:

Billboard specs
Current marketing material advertising sale (and all relevant data)
An idea that is from an American furniture store that I think is interesting

Target Market(s)

Upper middle class, sophisticated client who appreciates the finer things in life.

Industry/Entity Type

Furniture Store

Font styles to use
Sans Serif

Requirements
Must have
• Company Logo
• Winter Sales Event - 20 to 60% off
• Address: 3847 22nd Ave SW
Nice to have
• Image of furniture -- see our website www.maplewoven.ca -- any photo from this site can be used
Should not have
• Too much text or visual distration

```html
<!DOCTYPE html>
<html lang="en">
<head>
<meta charset="utf-8">
<title>Winter Sales Event Billboard — Maple Woven</title>
<link rel="stylesheet" href="https://fonts.googleapis.com/css2?family=Montserrat:wght@300;400;500;700&display=swap">
<style>
  :root {
    --page-bg: #eceef0;
    --board-dark: #2f3740;
    --board-mid: #46505b;
    --board-light: #56616c;
    --text-main: #ffffff;
    --text-soft: #dfe3e7;
    --rule: rgba(255, 255, 255, 0.45);
  }
  * { margin: 0; padding: 0; box-sizing: border-box; }
  html, body {
    width: 1145px;
    height: 1200px;
    overflow: hidden;
    background: var(--page-bg);
    font-family: "Montserrat", sans-serif;
  }
  .billboard {
    position: absolute;
    left: 40px;
    top: 355px;
    width: 1065px;
    height: 490px;
    background:
      radial-gradient(ellipse 70% 80% at 50% 40%, var(--board-light) 0%, var(--board-mid) 45%, var(--board-dark) 100%);
    color: var(--text-main);
    text-align: center;
    box-shadow: 0 2px 6px rgba(0, 0, 0, 0.25);
  }
  .line {
    position: absolute;
    left: 0;
    right: 0;
    white-space: nowrap;
    line-height: 1;
    transform: translateY(-50%);
  }
  .event-title {
    top: 88px;
    font-size: 58px;
    font-weight: 300;
    letter-spacing: 1px;
  }
  .event-title strong { font-weight: 700; }
  .discount {
    top: 184px;
    font-size: 92px;
    font-weight: 700;
    letter-spacing: 1px;
  }
  .discount .connector {
    font-size: 62px;
    font-weight: 300;
    margin: 0 6px;
  }
  .divider {
    position: absolute;
    left: 107px;
    right: 107px;
    top: 261px;
    height: 2px;
    background: var(--rule);
  }
  .brand-name {
    top: 322px;
    font-size: 68px;
    font-weight: 300;
    letter-spacing: 8px;
    color: var(--text-soft);
  }
  .address {
    top: 408px;
    font-size: 40px;
    font-weight: 500;
    letter-spacing: 1px;
  }
</style>
</head>
<body>
  <section class="billboard" aria-label="Winter Sales Event billboard">
    <p class="line event-title">WINTER <strong>SALES</strong> EVENT</p>
    <p class="line discount">SAVE 20 <span class="connector">TO</span> 60%</p>
    <div class="divider"></div>
    <p class="line brand-name">MAPLE WOVEN</p>
    <p class="line address">3847 22ND AVE SW, CALGARY, AB</p>
  </section>
</body>
</html>
```